BRISK GUARD WEBSITE BANNER DESIGN OF AWESOME

Please take a look at the attached Banner. I want a redesign Idea. The requirements are below.

1)Must Use Website Background
2)Must Use Photo Provided
3)Must Include Button
4)Website the banner will be used on you can see the current at the bottom of the page: https://b.plomvarn.com

Target Market(s)

Anyone Seeking Security Guard Services

```html
<!DOCTYPE html>
<html lang="en">
<head>
<meta charset="utf-8">
<title>Brisk Guard – Website Banner</title>
<link href="https://fonts.googleapis.com/css2?family=Roboto:wght@300;400;500;700;900&display=swap" rel="stylesheet">
<style>
  :root {
    --page-bg: #e1e1e1;
    --blue: #1b4d7b;
    --blue-deep: #1c3660;
    --blue-band: #1a3a66;
    --blue-foot: #1d5689;
    --gold: #fbb117;
    --ink-dark: #1b2a3d;
    --white: #ffffff;
    --photo-top: #3c6a8e;
    --photo-mid: #1d3450;
    --photo-bottom: #0d1520;
  }
  * { box-sizing: border-box; margin: 0; padding: 0; }
  html, body {
    width: 1200px; height: 758px; overflow: hidden;
    background: var(--page-bg);
    font-family: "Roboto", Arial, sans-serif;
  }
  .banner {
    position: absolute; left: 0; top: 144px;
    width: 1200px; height: 470px;
    background: var(--blue);
    overflow: hidden;
    color: var(--white);
  }
  .banner-backdrop { position: absolute; inset: 0; }
  .headline {
    position: absolute; left: 48px; top: 38px;
    font-size: 84px; line-height: 70px; letter-spacing: -1px;
  }
  .headline span { display: block; }
  .headline .light { font-weight: 400; }
  .headline .bold { font-weight: 900; }
  .tagline {
    position: absolute; left: 50px; top: 265px;
    font-size: 28px; font-weight: 400;
  }
  .cta {
    position: absolute; left: 47px; top: 309px;
    width: 264px; height: 37px;
    display: flex; align-items: center; justify-content: center;
    color: var(--ink-dark); font-weight: 700; font-size: 26px;
    text-decoration: none;
  }
  .cta::before {
    content: ""; position: absolute; inset: 0;
    background: var(--gold);
    clip-path: polygon(7% 0, 100% 0, 93% 100%, 0 100%);
    box-shadow: 0 4px 8px rgba(0,0,0,.35);
    z-index: -1;
  }
  .cta { z-index: 1; }
  .cta svg { margin-left: 8px; }
  .features {
    position: absolute; left: 50px; top: 362px;
    display: flex; align-items: center;
  }
  .feature {
    display: flex; align-items: center; gap: 14px;
    font-size: 23px; font-weight: 500; line-height: 29px;
  }
  .divider {
    width: 2px; height: 62px; background: var(--white);
    margin: 0 28px;
  }
  .guard-shield { position: absolute; left: 0; top: 0; }
</style>
</head>
<body>
<section class="banner" aria-label="Brisk Guard security services banner">
  <svg class="banner-backdrop" width="1200" height="470" viewBox="0 0 1200 470" aria-hidden="true">
    <polygon points="0,0 267,0 215,178 0,178" fill="var(--blue-deep)"/>
    <polygon points="0,178 900,178 900,250 480,330 0,255" fill="var(--blue-band)" opacity=".75"/>
    <polygon points="1037,0 1200,0 1200,200 1080,120" fill="var(--blue-deep)"/>
    <rect x="0" y="449" width="1200" height="21" fill="var(--blue-foot)"/>
    <polygon points="0,0 75,0 0,75" fill="var(--gold)"/>
  </svg>

  <h1 class="headline">
    <span class="light">GET</span>
    <span class="bold">SECURED</span>
    <span class="light">TODAY</span>
  </h1>
  <p class="tagline">We take your security personal.</p>

  <a class="cta" href="https://b.plomvarn.com">GET STARTED
    <svg width="28" height="16" viewBox="0 0 28 16" aria-hidden="true"><path d="M1 8h24M18 1l7 7-7 7" fill="none" stroke="var(--ink-dark)" stroke-width="2.5"/></svg>
  </a>

  <div class="features">
    <div class="feature">
      <svg width="68" height="64" viewBox="0 0 68 64" aria-hidden="true" fill="none" stroke="var(--gold)" stroke-width="2.2">
        <rect x="4" y="8" width="60" height="42" rx="3"/>
        <path d="M1 50h66v6a3 3 0 0 1-3 3H4a3 3 0 0 1-3-3z"/>
        <circle cx="34" cy="26" r="22"/>
        <ellipse cx="34" cy="26" rx="10" ry="22"/>
        <path d="M12 26h44M15 15h38M15 37h38M34 4v44"/>
      </svg>
      <span>Client<br>Portal</span>
    </div>
    <div class="divider"></div>
    <div class="feature">
      <svg width="64" height="64" viewBox="0 0 64 64" aria-hidden="true" fill="none" stroke="var(--gold)" stroke-width="2.2">
        <path d="M2 16h34v36H2zM36 30h14l10 12v10H36"/>
        <circle cx="14" cy="56" r="5"/><circle cx="50" cy="56" r="5"/>
        <path d="M19 4l12 4v9c0 7-5 11-12 14-7-3-12-7-12-14V8z"/>
        <path d="M13 17l5 5 8-9"/>
        <path d="M38 8h12M42 14h14"/><circle cx="58" cy="24" r="2"/>
      </svg>
      <span>24x7<br>Dispatch</span>
    </div>
    <div class="divider"></div>
    <div class="feature">
      <svg width="58" height="66" viewBox="0 0 58 66" aria-hidden="true" fill="none" stroke="var(--gold)" stroke-width="2.2">
        <path d="M16 2h36a4 4 0 0 1 4 4v54a4 4 0 0 1-4 4H6a4 4 0 0 1-4-4V18z"/>
        <path d="M2 18h14V2"/>
        <path d="M10 38h26M10 45h26M10 52h20M40 58h10"/>
        <circle cx="44" cy="12" r="3"/><circle cx="40" cy="26" r="3"/><circle cx="46" cy="38" r="3"/>
        <path d="M47 12h6M43 26h10M49 38h4M44 15l-4 8M40 29l5 6"/>
      </svg>
      <span>No Binding<br>Contracts</span>
    </div>
  </div>

  <svg class="guard-shield" width="1200" height="470" viewBox="0 0 1200 470">
    <defs>
      <linearGradient id="photoTone" x1="0" y1="0" x2="0.4" y2="1">
        <stop offset="0" stop-color="var(--photo-top)"/>
        <stop offset="0.5" stop-color="var(--photo-mid)"/>
        <stop offset="1" stop-color="var(--photo-bottom)"/>
      </linearGradient>
    </defs>
    <path role="img" aria-label="Photo: security guard in a dark uniform shining a flashlight up a stairwell at night"
          d="M721 29 Q850 40 945 4 Q1045 40 1157 31 Q1160 300 933 462 Q760 330 721 29 Z"
          fill="url(#photoTone)" stroke="var(--gold)" stroke-width="6"/>
  </svg>
</section>
</body>
</html>
```